Tidecrest NZ Brand, Revenue, Promotions & Events

I need an innovative business card that pops my brand. I like the colours against darker gradients and i'm not afraid to be bold.

I run my own Business, Brand, Event & Promotion company. I specialise in breathing life into businesses and adding atmosphere to promotions and events. I am concept based lady that likes to test the boundaries and create stand out campaigns that connect with the consumer.

I have 12 years business experience in a realm of interesting fields form 11 years in coordinating international music festivals & promotions, 6 years in radio with 8 radio awards including a NZ radio award for best sales team in NZ and was the national brand and sales manager for New Zealands 1st indoor entertainment mall. With 10 years of experience in advertising sales, I have an eye for creating revenue streams for businesses and thrive on implementing campaigns that compliment those streams.

I love sayings like "Do what you love, love what you do" and believe that you can achieve anything you want.

I have been fortunate in my career that my connections have carried me without needing to promote my business however it is important that I start to do so.

Target Market(s)

Decision makers 25 to 54

Contact Information for Business Card

Petra Ollingham
Director
p. 022 587 3091
e. petra@tidecrest.nz
www.tidecrest.nz

FB, IG and Linkedin logo

Font styles to use
Sans Serif

Colors

Designer to choose colors to be used in the design.

Requirements
Must have
• Petra Ollingham
• Director
• p. 022 587 3091
• e. petra@tidecrest.nz
• www.tidecrest.nz
• FB, IG and Linkedin logo
Nice to have
• I am looking for a business card with character, that leaves my presence with my customer and makes them remember my brand & optimistic personality when i walk out the door.

```html
<!DOCTYPE html>
<html lang="en">
<head>
<meta charset="utf-8">
<title>Tidecrest NZ Business Card</title>
<link rel="stylesheet" href="https://fonts.googleapis.com/css2?family=Montserrat:wght@500;600&family=Open+Sans:wght@400;600&family=Tinos:wght@700&display=swap">
<style>
  :root {
    --backdrop: #232323;
    --brand-blue: #2caae1;
    --brand-blue-deep: #1f8fc2;
    --card-white: #ffffff;
    --ink: #3a3a3a;
    --tagline-grey: #9a9a9a;
  }
  * { margin: 0; padding: 0; box-sizing: border-box; }
  html, body {
    width: 1200px; height: 900px; overflow: hidden;
    background: var(--backdrop);
  }
  .canvas {
    position: relative; width: 1200px; height: 900px;
  }
  .card {
    position: absolute; left: 320px; width: 560px; height: 320px;
    border-radius: 16px;
    box-shadow: 0 14px 30px rgba(0,0,0,0.45);
  }
  .card--front { top: 110px; background: var(--brand-blue); }
  .card--back { top: 470px; background: var(--card-white); }

  .brand {
    position: absolute;
    font-family: "Montserrat", sans-serif;
  }
  .brand__name {
    display: flex; align-items: center; gap: 10px;
    font-weight: 600; letter-spacing: 4px; text-transform: uppercase;
  }
  .brand__dot { border-radius: 50%; flex: none; }
  .brand__tagline {
    font-weight: 500; text-transform: uppercase; letter-spacing: 1px;
  }

  .card--front .brand { left: 0; right: 0; top: 118px; text-align: center; }
  .card--front .brand__name { justify-content: center; color: var(--card-white); font-size: 38px; }
  .card--front .brand__dot { width: 22px; height: 22px; background: var(--card-white); }
  .card--front .brand__tagline { color: var(--card-white); font-size: 14px; margin-top: 8px; }

  .card--back .brand { left: 34px; top: 150px; }
  .card--back .brand__name { color: var(--brand-blue); font-size: 23px; letter-spacing: 2.5px; gap: 7px; }
  .card--back .brand__dot { width: 14px; height: 14px; background: var(--brand-blue); }
  .card--back .brand__tagline { color: var(--tagline-grey); font-size: 8.5px; margin-top: 5px; }

  .divider {
    position: absolute; left: 296px; top: 92px; width: 1px; height: 110px;
    background: var(--brand-blue);
  }
  .contact {
    position: absolute; left: 318px; top: 92px;
    font-family: "Open Sans", sans-serif; color: var(--ink);
  }
  .contact__name {
    font-family: "Tinos", serif; font-weight: 700;
    color: var(--brand-blue); font-size: 21px; line-height: 1.1;
  }
  .contact__role { font-size: 13px; margin-top: 2px; margin-bottom: 10px; }
  .contact__list { list-style: none; }
  .contact__item {
    display: flex; align-items: center; gap: 8px;
    font-size: 12.5px; line-height: 20px;
  }
  .contact__icon { width: 10px; height: 10px; flex: none; }
</style>
</head>
<body>
<main class="canvas">
  <section class="card card--front" aria-label="Card front">
    <div class="brand">
      <div class="brand__name"><span class="brand__dot"></span>Tidecrest NZ</div>
      <div class="brand__tagline">Brand | Revenue | Events &amp; Promotions</div>
    </div>
  </section>

  <section class="card card--back" aria-label="Card back">
    <div class="brand">
      <div class="brand__name"><span class="brand__dot"></span>Tidecrest NZ</div>
      <div class="brand__tagline">Brand | Revenue | Events &amp; Promotions</div>
    </div>
    <div class="divider"></div>
    <div class="contact">
      <div class="contact__name">Petra Ollingham</div>
      <div class="contact__role">Director</div>
      <ul class="contact__list">
        <li class="contact__item">
          <svg class="contact__icon" viewBox="0 0 10 10" aria-hidden="true"><path d="M2 1 L4 1 L4.6 3 L3.4 4 Q4.4 5.8 6 6.6 L7 5.4 L9 6 L9 8 Q8.5 9 7.5 9 Q1 8 1 2.5 Q1 1.5 2 1Z" fill="#2caae1"/></svg>
          022 587 3091
        </li>
        <li class="contact__item">
          <svg class="contact__icon" viewBox="0 0 10 10" aria-hidden="true"><rect x="0.5" y="2" width="9" height="6" fill="#2caae1"/><path d="M0.5 2 L5 5.5 L9.5 2" stroke="#fff" stroke-width="0.9" fill="none"/></svg>
          petra@tidecrest.nz
        </li>
        <li class="contact__item">
          <svg class="contact__icon" viewBox="0 0 10 10" aria-hidden="true"><circle cx="5" cy="5" r="4.5" fill="#2caae1"/><path d="M0.5 5 H9.5 M5 0.5 Q2.5 5 5 9.5 M5 0.5 Q7.5 5 5 9.5" stroke="#fff" stroke-width="0.7" fill="none"/></svg>
          www.tidecrest.nz
        </li>
      </ul>
    </div>
  </section>
</main>
</body>
</html>
```